Welding Fabrication and Inspection Business Card Design

Welding Fabrication and Inspection Services,

Business

Industrial Machinery ServicesMohammed Rahim30 Ballarat Street, Brenmoor Heights East.5190.KVR

```html
<!DOCTYPE html>
<html lang="en">
<head>
<meta charset="utf-8">
<title>Tarnwell Forge Services – Business Card</title>
<link rel="stylesheet" href="https://fonts.googleapis.com/css2?family=Arimo:wght@400;700&display=swap">
<style>
  :root {
    --card-white: #ffffff;
    --brand-red: #8c3036;
    --band-grey: #3f3f41;
    --text-dark: #2a2a2a;
    --logo-grey: #3a3a3a;
    --page-bg: #eeeeee;
  }
  * { margin: 0; padding: 0; box-sizing: border-box; }
  html, body { width: 1200px; height: 788px; overflow: hidden; background: var(--page-bg); }
  .card {
    position: relative;
    width: 1200px; height: 788px;
    background: var(--card-white);
    font-family: "Arimo", Arial, sans-serif;
    color: var(--text-dark);
    overflow: hidden;
  }
  .company-mark {
    position: absolute; left: 740px; top: 180px; width: 420px;
    display: flex; align-items: center; gap: 12px;
    font-size: 28px; font-weight: 700; color: var(--logo-grey);
    white-space: nowrap;
  }
  .company-mark .mark-square { width: 24px; height: 24px; background: var(--logo-grey); flex: none; }
  .holder-name {
    position: absolute; left: 118px; top: 184px;
    font-size: 36px; font-weight: 700; color: var(--brand-red);
    padding-bottom: 4px; border-bottom: 3px solid var(--brand-red);
  }
  .contact-list { position: absolute; left: 118px; top: 288px; list-style: none; }
  .contact-list li {
    display: flex; align-items: flex-start; gap: 16px;
    font-size: 30px; line-height: 36px; margin-bottom: 18px;
  }
  .contact-list svg { width: 30px; height: 34px; flex: none; fill: var(--brand-red); margin-top: 1px; }
  .tool-photo {
    position: absolute; left: 797px; top: 300px; width: 360px; height: 290px;
    background: radial-gradient(ellipse 60% 45% at 50% 40%, #9a3039 0%, #8a2c34 45%, #55554d 70%, #ffffff 100%);
  }
  .footer-band { position: absolute; left: 0; top: 600px; width: 1200px; height: 188px; }
  .footer-title {
    position: absolute; left: 0; top: 676px; width: 1200px; text-align: center;
    font-size: 46px; line-height: 56px; font-weight: 700; letter-spacing: 1px; color: var(--brand-red);
    -webkit-text-stroke: 2px var(--card-white); paint-order: stroke fill;
  }
</style>
</head>
<body>
<div class="card">
  <div class="company-mark"><span class="mark-square"></span>Tarnwell Forge Services</div>

  <div class="holder-name">Khalid Nasser</div>

  <ul class="contact-list">
    <li>
      <svg viewBox="0 0 24 24"><path d="M6.6 2.5c.6-.4 1.4-.2 1.8.4l2 3.2c.4.6.2 1.3-.3 1.8l-1.3 1c.9 2.3 2.7 4.6 4.8 6l1.3-1c.5-.4 1.3-.4 1.8.1l2.7 2.6c.5.5.5 1.4 0 1.9l-1.6 1.7c-.9.9-2.3 1.2-3.5.6C8.2 18.6 4.7 14 3.4 8.6c-.3-1.3.2-2.6 1.2-3.4z"/></svg>
      <span>123-456-7890</span>
    </li>
    <li>
      <svg viewBox="0 0 24 24"><path d="M7 1h10a2 2 0 0 1 2 2v18a2 2 0 0 1-2 2H7a2 2 0 0 1-2-2V3a2 2 0 0 1 2-2zm0 3v14h10V4zm5 15.5a1 1 0 1 0 0 2 1 1 0 0 0 0-2z"/></svg>
      <span>123-456-7888</span>
    </li>
    <li>
      <svg viewBox="0 0 24 24"><path d="M1 5h22v14H1zm2 2v.4l9 6 9-6V7zm0 2.8V17h18V9.8l-9 6z"/></svg>
      <span>name@companyname.com</span>
    </li>
    <li>
      <svg viewBox="0 0 24 24"><path d="M12 1a8 8 0 0 1 8 8c0 5.5-8 14-8 14S4 14.5 4 9a8 8 0 0 1 8-8zm0 4.5a3.5 3.5 0 1 0 0 7 3.5 3.5 0 0 0 0-7z"/></svg>
      <span>17 Corrowen Street, Brenmoor Heights East.<br>5190.KVR</span>
    </li>
  </ul>

  <div class="tool-photo" role="img" aria-label="Photo of a red magnetic particle inspection yoke with hinged legs"></div>

  <svg class="footer-band" viewBox="0 0 1200 188" preserveAspectRatio="none" aria-hidden="true">
    <polygon fill="var(--band-grey)" points="0,30 40,22 70,34 110,18 150,28 190,16 230,30 270,20 310,32 350,14 390,26 430,18 470,30 510,12 550,24 590,16 630,28 670,14 710,26 750,10 790,22 830,16 870,28 910,12 950,24 990,18 1030,30 1070,14 1110,26 1150,18 1200,28 1200,152 0,152"/>
    <rect x="0" y="152" width="1200" height="36" fill="var(--brand-red)"/>
  </svg>
  <div class="footer-title">Tarnwell Forge Services</div>
</div>
</body>
</html>
```